New Business Card Design Project VORASTI-Italy

we are VORASTI-Italy
our company in the market for 3 years we are luxury cosmetic company and its about time for a facelift :)
i will like to have elegant luxurious and unique business card
that will give the person that get it a unique, luxurious and elegant impression
I'm VERY OPEN FOR NEW IDEAS , even duo i add a few files of things that i see on line and i like them

i add my logo as well
my website is VORASTI.COM
(if you would like to see the main style that we have)

Target Market(s)

adult that have money :)

Industry/Entity Type

Business

Contact Information for Business Card

Name - Paul Vorasti
Position - CEO and CO Founder
address - 4817 E Larkdale
telephone - 555-384-1962
email - paul@vorasti.com
fax - 555-384-1962
website - VORASTI.COM

Colors
000000
959595
fbee3e
ffffff

Requirements
Must have
• big logo in GOLD color
• elegant look
• impressive
Nice to have
• not must but maybe classy pattern background
• not must but maybe emblem
• maybe clear plastic business card
Should not have
• colors
• images

```html
<!DOCTYPE html>
<html lang="en">
<head>
<meta charset="utf-8">
<title>VORASTI Italy – Business Card</title>
<link rel="stylesheet" href="https://fonts.googleapis.com/css2?family=Quicksand:wght@500;700&display=swap">
<style>
  :root {
    --stage: #cacacf;
    --card: #282624;
    --card-deep: #211f1e;
    --gold: #cfa935;
    --fold: #151413;
  }
  * { margin: 0; padding: 0; box-sizing: border-box; }
  html, body {
    width: 1200px;
    height: 1200px;
    overflow: hidden;
    background: var(--stage);
    font-family: "Quicksand", sans-serif;
  }
  .canvas { position: relative; width: 1200px; height: 1200px; }

  .card {
    position: absolute;
    left: 264px;
    width: 674px;
    height: 405px;
    border-radius: 16px;
    background: var(--card);
    overflow: hidden;
    color: var(--gold);
  }
  .card--front { top: 158px; }
  .card--back  { top: 629px; }

  .quilt-texture {
    position: absolute;
    inset: 0;
    background: radial-gradient(ellipse at 50% 45%, #302d2b 0%, var(--card) 55%, var(--card-deep) 100%);
  }

  .brand {
    position: absolute;
    left: 0; right: 0;
    top: 0; bottom: 0;
    text-align: center;
  }
  .brand__ring {
    position: absolute;
    left: 50%;
    top: 56px;
    width: 152px;
    height: 152px;
    margin-left: -76px;
    border: 4px solid var(--gold);
    border-radius: 50%;
  }
  .brand__name {
    position: absolute;
    left: 0; right: 0;
    top: 228px;
    font-size: 68px;
    font-weight: 700;
    letter-spacing: 2px;
    line-height: 1;
  }
  .brand__rule {
    position: absolute;
    left: 174px;
    width: 334px;
    top: 318px;
    height: 4px;
    background: var(--gold);
  }
  .brand__origin {
    position: absolute;
    left: 0; right: 0;
    top: 334px;
    font-size: 27px;
    font-weight: 700;
    letter-spacing: 1px;
    line-height: 1;
  }

  .holder {
    position: absolute;
    left: 56px;
    top: 158px;
  }
  .holder__name {
    font-size: 29px;
    font-weight: 700;
    letter-spacing: 0.3px;
    line-height: 1.15;
  }
  .holder__role {
    font-size: 19px;
    font-weight: 500;
    margin-top: 4px;
  }

  .fold {
    position: absolute;
    left: 392px;
    top: 0;
    bottom: 0;
    width: 10px;
    background: linear-gradient(90deg, rgba(21,20,19,0) 0%, var(--fold) 70%, rgba(21,20,19,0) 100%);
    opacity: 0.8;
  }

  .contact {
    position: absolute;
    left: 422px;
    top: 96px;
    list-style: none;
  }
  .contact__item {
    font-size: 21px;
    font-weight: 500;
    line-height: 1;
    height: 48px;
    white-space: nowrap;
  }
</style>
</head>
<body>
<div class="canvas">

  <section class="card card--front">
    <div class="quilt-texture" role="img" aria-label="Subtle quilted diamond stitch pattern in dark charcoal"></div>
    <div class="brand">
      <div class="brand__ring"></div>
      <div class="brand__name">VORASTI</div>
      <div class="brand__rule"></div>
      <div class="brand__origin">ITALY</div>
    </div>
  </section>

  <section class="card card--back">
    <div class="holder">
      <div class="holder__name">PAUL VORASTI</div>
      <div class="holder__role">CEO and CO Founder</div>
    </div>
    <div class="fold"></div>
    <ul class="contact">
      <li class="contact__item">4817 E Larkdale</li>
      <li class="contact__item">555-384-1962</li>
      <li class="contact__item">paul@vorasti.com</li>
      <li class="contact__item">555-384-1962</li>
      <li class="contact__item">VORASTI.COM</li>
    </ul>
  </section>

</div>
</body>
</html>
```